Zielgruppe
Firma: Spirituosen Großhandel
Zielgruppe: Junge
Aufgabenstellung
Produkt: Gin 40%, 0,7L
Marke: Falke GIN oder 7R GIN (7 roots herbal blend)
Ursprung: Deutschland
Geschmack: frisch, mild, geschmeidig und weich
Der Gin könnten zwei Idee sein.
1. Falke Gin, da der Geschmack frisch, mild, rein ist.
2. 7R Gin, da der aus 18 verschiedenen Pflanzen destilliert wird. (englich. 7 Roots Pflanzen bzw. 7R)
Wacholder, Zitrusfrüchte, Ingwer, Kirschblüte, schwarzer Pfeffer, Minze, grüner Tee, Grapefruit usw.
Seite: Vor-, Rückseite und Kapsel/Halsetikett
Material: Papier oder Plastikfolie
Art: modern oder klassisch, hochwertig und Auffällig!!!
Flaschtyp: 2 Glass Durchsichtig (im Anhang)
Eigenschaften: Fluoreszierender Teil auf dem Etikett
Hochwertig wegen Primium Qualität
Flasche und Etikett passen miteinander

```html
<!DOCTYPE html>
<html lang="de">
<head>
<meta charset="utf-8">
<title>Korvel Gin – Etikett</title>
<link rel="stylesheet" href="https://fonts.googleapis.com/css2?family=Titillium+Web:wght@300;700&display=swap">
<style>
  :root {
    --paper: #ffffff;
    --band: #2b2b2b;
    --band-deep: #242424;
    --wave-blue: #2f5fbf;
    --wave-light: #c9d6f0;
    --glow-blue: 61, 111, 224;
    --brand-silver: #d2d5db;
    --fine-text: #3a3a3a;
  }
  html, body {
    margin: 0;
    padding: 0;
    width: 1200px;
    height: 2400px;
    overflow: hidden;
    background: var(--paper);
    font-family: "Titillium Web", sans-serif;
  }
  .canvas {
    position: relative;
    width: 1200px;
    height: 2400px;
  }

  .glow {
    position: absolute;
    z-index: 0;
  }
  .brand {
    position: absolute;
    left: 0;
    right: 0;
    z-index: 1;
    text-align: center;
    color: var(--brand-silver);
    line-height: 1;
  }
  .brand-name {
    display: block;
    font-weight: 700;
    text-transform: uppercase;
    letter-spacing: 0.04em;
  }
  .brand-sub {
    display: block;
    font-weight: 300;
  }

  /* Halsetikett */
  .neck-label {
    position: absolute;
    left: 472px;
    top: 256px;
    width: 256px;
    height: 464px;
    background: var(--band);
    border-radius: 20px 20px 0 0;
    overflow: hidden;
  }
  .neck-label .brand { top: 296px; }
  .neck-label .brand-name { font-size: 60px; }
  .neck-label .brand-sub { font-size: 34px; margin-top: 2px; }
  .neck-label .glow {
    left: 0;
    right: 0;
    bottom: 0;
    height: 110px;
    background: radial-gradient(ellipse 70% 60% at 65% 65%, rgba(var(--glow-blue), 0.85) 0%, rgba(var(--glow-blue), 0.25) 50%, rgba(var(--glow-blue), 0) 80%);
  }

  /* Frontetikett */
  .front-label {
    position: absolute;
    left: 288px;
    top: 912px;
    width: 640px;
    height: 1120px;
  }
  .wave-field {
    position: absolute;
    left: 0;
    right: 0;
  }
  .wave-field--top {
    top: 0;
    height: 248px;
    background: linear-gradient(180deg, rgba(201,214,240,0.35) 0%, rgba(47,95,191,0.45) 100%);
  }
  .wave-field--bottom {
    top: 536px;
    height: 472px;
    background: linear-gradient(180deg, rgba(47,95,191,0.45) 0%, rgba(201,214,240,0.15) 100%);
  }
  .brand-band {
    position: absolute;
    left: 0;
    right: 0;
    top: 248px;
    height: 288px;
    background: linear-gradient(180deg, var(--band) 0%, var(--band-deep) 100%);
    overflow: hidden;
  }
  .brand-band .brand { top: 52px; }
  .brand-band .brand-name { font-size: 118px; }
  .brand-band .brand-sub { font-size: 64px; margin-top: 4px; }
  .brand-band .glow {
    left: 0;
    right: 0;
    bottom: 0;
    height: 120px;
    background: radial-gradient(ellipse 60% 70% at 78% 90%, rgba(var(--glow-blue), 0.9) 0%, rgba(var(--glow-blue), 0.3) 45%, rgba(var(--glow-blue), 0) 80%);
  }

  .product-facts {
    position: absolute;
    left: 0;
    right: 0;
    top: 1040px;
    margin: 0;
    display: flex;
    justify-content: center;
    gap: 72px;
    font-weight: 300;
    font-size: 29px;
    line-height: 1;
    color: var(--fine-text);
  }
</style>
</head>
<body>
<main class="canvas">

  <section class="neck-label">
    <div class="glow" role="img" aria-label="Fluoreszierender blauer Rauchschleier"></div>
    <div class="brand">
      <span class="brand-name">Korvel</span>
      <span class="brand-sub">Gin</span>
    </div>
  </section>

  <section class="front-label">
    <div class="wave-field wave-field--top" role="img" aria-label="Muster aus blauen Wellenlinien"></div>

    <div class="brand-band">
      <div class="glow" role="img" aria-label="Fluoreszierender blauer Rauchschleier"></div>
      <div class="brand">
        <span class="brand-name">Korvel</span>
        <span class="brand-sub">Gin</span>
      </div>
    </div>

    <div class="wave-field wave-field--bottom" role="img" aria-label="Muster aus blauen Wellenlinien"></div>

    <p class="product-facts">
      <span class="abv">Gin 40%</span>
      <span class="volume">0,7L</span>
    </p>
  </section>

</main>
</body>
</html>
```